Building Servicess

We need a new business card design for a company. We specialise in: Electrical/Site temporary electrics, Data/Network Installation, Passive Fire Protection

Industry/Entity Type

Construction

Contact Information for Business Card

Services provided as detailed on project description

Font styles to use
Serif

Colors
0054AA
0677BA
7BADD7
CADEEF
E8F1F8
00AB8E
00BBA5
67D7C9
C6EFE9
E9F9F6
EB3D1F
EC4F4E
F09395
F8D3D4
FCEDEE

Requirements
Must have
• Company logo-contact details-phone numbers

```html
<!DOCTYPE html>
<html lang="en">
<head>
<meta charset="utf-8">
<title>Norvale Site Services – Business Card</title>
<link rel="stylesheet" href="https://fonts.googleapis.com/css2?family=Poppins:wght@500;600&family=Roboto:wght@500&display=swap">
<style>
  :root {
    --backdrop: #6e5a43;
    --card: #050607;
    --brand-blue: #0677ba;
    --band-blue: #0a76b8;
    --white: #ffffff;
    --rule-grey: #9a9a9a;
    --ink: #0b0b0b;
  }
  * { margin: 0; padding: 0; box-sizing: border-box; }
  html, body { width: 900px; height: 1200px; overflow: hidden; }
  body {
    position: relative;
    background: var(--backdrop);
    font-family: "Poppins", sans-serif;
  }
  .card {
    position: absolute;
    width: 773px;
    height: 448px;
    background: var(--card);
    border-radius: 22px;
    overflow: hidden;
  }
  .card--front { left: 72px; top: 135px; }
  .card--back { left: 74px; top: 624px; height: 449px; }

  .brand {
    position: absolute;
    left: 0; right: 0; top: 228px;
    display: flex;
    flex-direction: column;
    align-items: center;
  }
  .brand__name {
    color: var(--brand-blue);
    font-weight: 600;
    font-size: 40px;
    letter-spacing: 0.5px;
    line-height: 1;
    display: flex;
    align-items: center;
    gap: 14px;
  }
  .brand__mark {
    width: 22px; height: 22px;
    background: var(--brand-blue);
  }
  .brand__rule {
    margin-top: 52px;
    width: 443px;
    height: 44px;
    position: absolute;
    top: 0;
  }
  .brand__lockup { position: relative; display: flex; flex-direction: column; align-items: center; }
  .brand__divider {
    width: 400px; height: 2px; background: var(--rule-grey); margin-top: 14px;
  }
  .services-band {
    position: absolute;
    left: 0; right: 0; top: 355px;
    height: 55px;
    background: var(--band-blue);
    display: flex;
    flex-direction: column;
    justify-content: center;
    align-items: center;
    font-family: "Roboto", sans-serif;
    font-weight: 500;
    font-size: 16px;
    letter-spacing: 1.6px;
    line-height: 21px;
    color: var(--ink);
    text-align: center;
  }
  .services-band span:last-child { color: var(--white); }

  .holder {
    position: absolute;
    left: 0; right: 0; top: 86px;
    text-align: center;
  }
  .holder__name {
    color: var(--brand-blue);
    font-weight: 600;
    font-size: 29px;
    letter-spacing: 1.5px;
    line-height: 36px;
  }
  .holder__role {
    color: var(--white);
    font-weight: 600;
    font-size: 22px;
    letter-spacing: 2px;
    line-height: 30px;
  }
  .contact-icons {
    position: absolute;
    left: 0; top: 196px;
    width: 773px; height: 44px;
  }
  .contacts {
    position: absolute;
    left: 0; right: 0; top: 280px;
    text-align: center;
    font-family: "Roboto", sans-serif;
    font-weight: 500;
    font-size: 20px;
    letter-spacing: 0.8px;
    line-height: 32px;
    color: var(--white);
  }
  .contacts__email { color: var(--brand-blue); }
</style>
</head>
<body>
  <section class="card card--front">
    <div class="brand">
      <div class="brand__lockup">
        <div class="brand__name"><span class="brand__mark"></span>NORVALE SITE SERVICES LTD</div>
        <div class="brand__divider"></div>
      </div>
    </div>
    <div class="services-band">
      <span>ELECTRICAL/SITE TEMPORARY ELECTRICS,</span>
      <span>DATA/NETWORK INSTALLATION, PASSIVE FIRE PROTECTION</span>
    </div>
  </section>

  <section class="card card--back">
    <div class="holder">
      <p class="holder__name">JOHNATHAN DOE</p>
      <p class="holder__role">DIRECTOR</p>
    </div>

    <svg class="contact-icons" viewBox="0 0 773 44" aria-hidden="true">
      <path d="M209 22 L306 21 L209 20 Z" fill="#ffffff"/>
      <path d="M467 21 L566 20 L566 22 Z" fill="#ffffff"/>
      <g fill="#ffffff">
        <circle cx="333" cy="22" r="18"/>
        <circle cx="386" cy="22" r="18"/>
        <circle cx="438" cy="22" r="18"/>
      </g>
      <path class="icon-phone" fill="#0b0b0b"
        d="M326 13 c1.5-1 3-0.5 3.5 0.8 l1.5 3.2 c0.4 1-0.1 2-0.9 2.6 l-1 0.7 c0.8 2.2 2.6 4.2 4.8 5.2 l0.8-1 c0.7-0.8 1.7-1 2.6-0.5 l3 1.8 c1.2 0.7 1.4 2.2 0.5 3.4 l-1 1.2 c-1.3 1.4-3.5 1.7-5.4 0.8 c-4.5-2.2-8-6-9.8-10.6 c-0.7-1.9-0.3-3.9 1-5.2 Z"/>
      <g class="icon-mail">
        <rect x="377" y="15" width="18" height="14" rx="2" fill="#0b0b0b"/>
        <path d="M378.5 17 L386 23 L393.5 17" fill="none" stroke="#ffffff" stroke-width="1.6"/>
      </g>
      <g class="icon-globe" fill="none" stroke="#0b0b0b" stroke-width="1.6">
        <circle cx="438" cy="22" r="9"/>
        <ellipse cx="438" cy="22" rx="4" ry="9"/>
        <line x1="429" y1="22" x2="447" y2="22"/>
        <path d="M430.5 17.5 H445.5 M430.5 26.5 H445.5"/>
      </g>
    </svg>

    <div class="contacts">
      <p>+123 456 7890</p>
      <p class="contacts__email">email@norvalesiteservices.com</p>
      <p>www.norvalesiteservices.com</p>
    </div>
  </section>
</body>
</html>
```